New Business Card Design Project

2 sided business card required. I have attached some previous designs of items we have had made so you can see the logo etc. we Want the card to look professional and modern. for the final design upload for winning designer please note I need to be able to edit the names / phone numbers on the card design as I need to get them made for different staff.
Updates

extending time so designers can have time to submit

Target Market(s)

new customers

Industry/Entity Type

transport / earthmoving

Contact Information for Business Card

name, phone number email address

Requirements
Nice to have
• professional / impressive looking card (first impressions to customers count)
Should not have
• do not put our mobile number on the design use a generic number

```html
<!DOCTYPE html>
<html lang="en">
<head>
<meta charset="utf-8">
<title>RHT Pty Ltd – Business Card</title>
<link rel="stylesheet" href="https://fonts.googleapis.com/css2?family=Rajdhani:wght@600;700&family=Hind:wght@500;600&display=swap">
<style>
  :root {
    --page-bg: #1d1d1f;
    --card-black: #0e0e0f;
    --silver: #c9cbcf;
    --gold-dark: #b9892c;
    --gold-mid: #e7c766;
    --gold-light: #fff2b0;
    --ink: #111111;
    --white: #ffffff;
  }
  * { box-sizing: border-box; margin: 0; padding: 0; }
  html, body { width: 1200px; height: 900px; overflow: hidden; }
  body { background: var(--page-bg); position: relative; font-family: "Hind", sans-serif; }

  .card {
    position: absolute;
    border-radius: 18px;
    overflow: hidden;
    background: var(--card-black);
  }
  .card--front { left: 271px; top: 60px; width: 654px; height: 372px; }
  .card--back  { left: 269px; top: 470px; width: 658px; height: 376px; }

  .photo { position: absolute; left: 0; top: 0; width: 100%; }
  .card--front .photo {
    height: 238px;
    background:
      linear-gradient(115deg, rgba(255,255,255,0) 58%, rgba(255,255,255,0.10) 66%, rgba(255,255,255,0) 76%),
      linear-gradient(180deg, #0c0c0d 0%, #1c1c1e 30%, #2f2f31 52%, #1a1a1b 66%, #242426 82%, #4a4a4c 94%, #5a5a5c 100%);
  }
  .card--back .photo {
    height: 258px;
    background:
      linear-gradient(115deg, rgba(255,255,255,0) 58%, rgba(255,255,255,0.10) 66%, rgba(255,255,255,0) 76%),
      linear-gradient(180deg, #0b0b0c 0%, #1d1d1f 28%, #2a2a2c 44%, #1a1a1b 58%, #3a3230 70%, #8f6242 80%, #b47c50 90%, #9a6842 100%);
  }

  .brand {
    position: absolute;
    left: 0; width: 100%;
    text-align: center;
    font-family: "Rajdhani", sans-serif;
    font-weight: 700;
    color: var(--silver);
  }
  .brand__mark { display: block; font-size: 104px; line-height: 0.9; letter-spacing: 14px; text-indent: 14px; }
  .brand__suffix { font-size: 18px; line-height: 1; }
  .card--front .brand { top: 20px; }
  .card--front .brand__suffix { display: block; margin-top: 2px; }
  .card--back .brand { top: 28px; }
  .card--back .brand__suffix { position: absolute; left: 460px; top: 88px; }

  .gold-band {
    position: absolute; left: 0; width: 100%;
    background: linear-gradient(100deg, var(--gold-dark) 0%, var(--gold-mid) 20%, var(--gold-light) 38%, var(--gold-mid) 55%, var(--gold-dark) 72%, var(--gold-mid) 88%, var(--gold-light) 100%);
  }
  .card--front .gold-band { top: 238px; height: 100px; border-bottom: 4px solid var(--ink); }
  .card--back .gold-band { top: 258px; height: 118px; border-top: 4px solid var(--ink); }

  .identity { position: absolute; right: 346px; top: 258px; text-align: right; font-family: "Rajdhani", sans-serif; font-weight: 700; color: var(--ink); }
  .identity__name { font-size: 32px; line-height: 1; letter-spacing: 0.5px; }
  .identity__role { font-family: "Hind", sans-serif; font-weight: 600; font-size: 17px; line-height: 1.4; }
  .divider { position: absolute; left: 327px; top: 248px; width: 2px; height: 80px; background: var(--ink); }

  .contacts { position: absolute; left: 344px; top: 248px; list-style: none; color: var(--ink); font-size: 19px; font-weight: 500; }
  .contacts li { display: flex; align-items: center; height: 27px; }
  .contacts svg { width: 18px; height: 18px; margin-right: 10px; flex: none; }

  .address {
    position: absolute; left: 0; top: 342px; width: 100%; height: 30px;
    background: var(--white); color: var(--ink);
    text-align: center; font-size: 19px; font-weight: 600; line-height: 32px;
  }

  .services-title {
    position: absolute; left: 222px; top: 243px; width: 214px; height: 37px;
    background: #1a1a1a; border-radius: 7px;
    font-family: "Rajdhani", sans-serif; font-weight: 700; font-size: 25px; letter-spacing: 1px;
    color: var(--gold-mid); text-align: center; line-height: 39px;
  }
  .services { position: absolute; top: 293px; list-style: none; font-family: "Rajdhani", sans-serif; font-weight: 700; font-size: 18.5px; color: var(--ink); }
  .services li { height: 20px; line-height: 20px; }
  .services li::before { content: "• "; }
  .services--one { left: 36px; }
  .services--two { left: 242px; }
  .services--three { left: 447px; }
  .services-rule { position: absolute; top: 298px; width: 2px; height: 54px; background: var(--ink); }
  .services-rule--a { left: 229px; }
  .services-rule--b { left: 435px; }
</style>
</head>
<body>

<section class="card card--front">
  <div class="photo" role="img" aria-label="Black and white photo of a road train tipper truck with three trailers against a dark hexagon-perforated metal texture"></div>
  <div class="brand"><span class="brand__mark">RHT</span><span class="brand__suffix">Pty Ltd</span></div>
  <div class="gold-band"></div>
  <div class="identity">
    <div class="identity__name">DANIEL HARPER</div>
    <div class="identity__role">Manager</div>
  </div>
  <div class="divider"></div>
  <ul class="contacts">
    <li><svg viewBox="0 0 20 20"><circle cx="10" cy="10" r="10" fill="#111"/><path d="M6.5 5.5l2 0 1 2.5-1.3 1a6 6 0 0 0 2.8 2.8l1-1.3 2.5 1v2a1 1 0 0 1-1 1A8.5 8.5 0 0 1 5.5 6.5a1 1 0 0 1 1-1z" fill="#e7c766"/></svg>123-456-2100</li>
    <li><svg viewBox="0 0 20 20"><circle cx="10" cy="10" r="10" fill="#111"/><rect x="5" y="6.5" width="10" height="7" fill="none" stroke="#e7c766" stroke-width="1.4"/><path d="M5 6.5l5 4 5-4" fill="none" stroke="#e7c766" stroke-width="1.4"/></svg>youremail@mailbox.com</li>
    <li><svg viewBox="0 0 20 20"><circle cx="10" cy="10" r="10" fill="#111"/><circle cx="10" cy="10" r="5.5" fill="none" stroke="#e7c766" stroke-width="1.3"/><ellipse cx="10" cy="10" rx="2.4" ry="5.5" fill="none" stroke="#e7c766" stroke-width="1.2"/><path d="M4.5 10h11" stroke="#e7c766" stroke-width="1.2"/></svg>www.yourwebsite.com</li>
  </ul>
  <div class="address">Your address, city, state, ZIP 0000</div>
</section>

<section class="card card--back">
  <div class="photo" role="img" aria-label="Colour photo of a road train tipper truck hauling three trailers on red outback dirt, beneath a dark hexagon-perforated metal texture"></div>
  <div class="brand"><span class="brand__mark">RHT</span><span class="brand__suffix">Pty Ltd</span></div>
  <div class="gold-band"></div>
  <div class="services-title">OUR SERVICES</div>
  <ul class="services services--one"><li>ROAD TRAIN TIPPERS</li><li>ROAD TRAIN TIPPERS</li><li>ROAD TRAIN TIPPERS</li></ul>
  <span class="services-rule services-rule--a"></span>
  <ul class="services services--two"><li>ROAD TRAIN TIPPERS</li><li>ROAD TRAIN TIPPERS</li><li>ROAD TRAIN TIPPERS</li></ul>
  <span class="services-rule services-rule--b"></span>
  <ul class="services services--three"><li>ROAD TRAIN TIPPERS</li><li>ROAD TRAIN TIPPERS</li><li>ROAD TRAIN TIPPERS</li></ul>
</section>

</body>
</html>
```